Letterhead & Business Card for our Professional Practice (Financial Services)

We are looking for someone to design a letterhead and business card for our business, which is a professional practice called Harbor Lumen Capital Limited. The website is at www.harborrlumencapital.example.co.uk.

The letterhead needs to have: (a) our logo (b) address (c) telephone number (d) email address and (e) our company number.

We would like the stationary to be consistent with the website.

I have attached the logo in EPS and PNG format.

Target Market(s)

Professional services, large commercial enterprises, financial services

Industry/Entity Type

Financial Service

Font styles to use
Serif

Colors
3176b5
f04a50

Requirements
Must have
• Be consistent with our website located at www.harborlumencapital.example.co.uk
• Be in the following formats:
• 1. Word template for the letterhead
• 2. PDF for the letterhead with setup and bleeds required at www.presskite.example.co.uk
• 3. PDF for the business card with setup and bleeds required at www.presskite.example.co.uk
Nice to have
• Something with a really interesting design that says "these guys are professional but dynamic and interesting"
Should not have
• Boring

```html
<!DOCTYPE html>
<html lang="en">
<head>
<meta charset="utf-8">
<title>Harbor Lumen Capital – Stationery</title>
<link rel="stylesheet" href="https://fonts.googleapis.com/css2?family=Cabin:wght@500&family=Source+Sans+3:wght@400;600&display=swap">
<style>
  :root {
    --navy: #1c3261;
    --red: #be2127;
    --paper: #ffffff;
    --backdrop: #cccccc;
    --text: #2a3558;
  }
  * { box-sizing: border-box; margin: 0; padding: 0; }
  html, body { width: 1200px; height: 1054px; overflow: hidden; }
  body {
    background: var(--backdrop);
    font-family: "Source Sans 3", sans-serif;
    color: var(--text);
    position: relative;
  }
  .brand-name {
    font-family: "Cabin", sans-serif;
    font-weight: 500;
    color: var(--navy);
    white-space: nowrap;
  }
  .brand-square { display: inline-block; background: var(--red); flex: none; }

  /* Letterhead */
  .letterhead {
    position: absolute; left: 168px; top: 121px;
    width: 573px; height: 811px;
    background: var(--paper);
    box-shadow: 0 0 2px rgba(0,0,0,.15);
    overflow: hidden;
  }
  .letterhead .brand {
    position: absolute; left: 0; right: 0; top: 69px;
    display: flex; align-items: center; justify-content: center; gap: 14px;
  }
  .letterhead .brand-square { width: 48px; height: 48px; }
  .letterhead .brand-name { font-size: 24px; }
  .letterhead .contact {
    position: absolute; left: 46px; top: 735px;
    list-style: none; font-size: 9.5px; line-height: 13.5px;
  }
  .contact li { display: flex; align-items: center; gap: 6px; white-space: nowrap; }
  .contact svg { width: 9px; height: 9px; flex: none; }
  .letterhead .footer-band { position: absolute; left: 0; bottom: 0; width: 573px; height: 37px; }
  .letterhead .footer-url {
    position: absolute; right: 28px; bottom: 11px;
    font-size: 10.5px; color: #fff; white-space: nowrap;
  }

  /* Business cards */
  .card {
    position: absolute; left: 784px; width: 249px; height: 150px;
    background: var(--paper); overflow: hidden;
    box-shadow: 0 0 2px rgba(0,0,0,.15);
  }
  .card-front { top: 220px; }
  .card-front .brand {
    position: absolute; left: 0; right: 0; top: 33px;
    display: flex; flex-direction: column; align-items: center; gap: 8px;
  }
  .card-front .brand-square { width: 44px; height: 44px; }
  .card-front .brand-name { font-size: 17px; }
  .card-front .tagline {
    position: absolute; left: 0; bottom: 0; width: 100%; height: 20px;
    background: var(--navy); color: #fff;
    font-size: 5.5px; text-align: center; line-height: 20px;
  }
  .card-back { top: 389px; }
  .card-back .swoosh { position: absolute; inset: 0; }
  .card-back .brand {
    position: absolute; left: 15px; top: 16px;
    display: flex; align-items: center; gap: 7px;
  }
  .card-back .brand-square { width: 41px; height: 41px; }
  .card-back .brand-name { font-size: 12.5px; }
  .card-back .contact {
    position: absolute; left: 15px; top: 89px;
    list-style: none; font-size: 5.5px; line-height: 10px;
  }
  .card-back .contact svg { width: 6px; height: 6px; }
  .card-back .address { position: absolute; left: 15px; top: 119px; font-size: 5.5px; line-height: 10px; }
  .card-back .person { position: absolute; right: 16px; top: 118px; text-align: right; color: #fff; }
  .person .name { font-family: "Cabin", sans-serif; font-size: 9px; }
  .person .title { font-size: 5.5px; margin-top: 2px; }
</style>
</head>
<body>

<section class="letterhead" aria-label="Letterhead">
  <div class="brand">
    <span class="brand-square"></span>
    <span class="brand-name">Harbor Lumen Capital</span>
  </div>

  <ul class="contact">
    <li><svg viewBox="0 0 10 10" fill="none" stroke="#be2127" stroke-width="1"><path d="M2 1 L4 1 L4.5 3 L3.3 4 Q4.5 6 6 6.7 L7 5.5 L9 6 L9 8 Q5 9 2 5 Q1 3 2 1 Z"/></svg>01632 960418</li>
    <li><svg viewBox="0 0 10 10" fill="none" stroke="#be2127" stroke-width="1"><rect x="1" y="2" width="8" height="6"/><path d="M1 2 L5 5.5 L9 2"/></svg>contact@harborlumencapital.example.co.uk</li>
    <li><svg viewBox="0 0 10 10" fill="none" stroke="#be2127" stroke-width="1"><path d="M5 9.5 Q1.5 5.5 1.5 4 A3.5 3.5 0 0 1 8.5 4 Q8.5 5.5 5 9.5 Z"/><circle cx="5" cy="4" r="1.2"/></svg>14-15 Quayside Row Marlow Berkshire SL7 2QX</li>
  </ul>

  <svg class="footer-band" viewBox="0 0 573 37" aria-hidden="true">
    <rect x="0" y="19" width="573" height="18" fill="#1c3261"/>
    <polygon points="300,0 573,0 573,37 274,37" fill="#be2127"/>
  </svg>
  <span class="footer-url">www.harborlumencapital.example.co.uk</span>
</section>

<section class="card card-front" aria-label="Business card front">
  <div class="brand">
    <span class="brand-square"></span>
    <span class="brand-name">Harbor Lumen Capital</span>
  </div>
  <p class="tagline">These guys are professional but dynamic and interesting</p>
</section>

<section class="card card-back" aria-label="Business card back">
  <svg class="swoosh" viewBox="0 0 249 150" aria-hidden="true">
    <path d="M182 0 C230 28 232 112 84 150 L92 150 C238 112 238 28 192 0 Z" fill="#be2127"/>
    <path d="M200 0 C246 34 236 115 106 150 L249 150 L249 0 Z" fill="#1c3261"/>
  </svg>
  <div class="brand">
    <span class="brand-square"></span>
    <span class="brand-name">Harbor Lumen Capital</span>
  </div>
  <ul class="contact">
    <li><svg viewBox="0 0 10 10" fill="none" stroke="#be2127" stroke-width="1"><path d="M2 1 L4 1 L4.5 3 L3.3 4 Q4.5 6 6 6.7 L7 5.5 L9 6 L9 8 Q5 9 2 5 Q1 3 2 1 Z"/></svg>01632 960418</li>
    <li><svg viewBox="0 0 10 10" fill="none" stroke="#be2127" stroke-width="1"><rect x="1" y="2" width="8" height="6"/><path d="M1 2 L5 5.5 L9 2"/></svg>www.harborlumencapital.example.co.uk</li>
    <li><svg viewBox="0 0 10 10" fill="none" stroke="#be2127" stroke-width="1"><circle cx="5" cy="5" r="4"/><path d="M1 5 H9 M5 1 Q2.5 5 5 9 Q7.5 5 5 1"/></svg>contact@harborlumencapital.example.co.uk</li>
  </ul>
  <p class="address">14-15 Quayside Row Marlow<br>Berkshire SL7 2QX</p>
  <div class="person">
    <p class="name">Your name</p>
    <p class="title">Your Title</p>
  </div>
</section>

</body>
</html>
```